Dyslexia Assessment Business card design

we need a business card design for a new company based in New Hampshire called Maple Path Learning of NH. We provide dyslexia assessment and consultation
Updates

Can you please add my degrees/certifications Carla Whitmore MA, MEd NH Certified Specialist in the Assessment of Intellectual Functioning Reading and Writing Specialist Learning Disabilities Specialist

I am interested in also creating a web page. If you have experience with webpages that may be useful. I have the domains but am waiting the name of the business to be cleared by the state. I expect this to take place within the month.

I think listing all the certifications is too much. Please just add Carla Whitmore MA, MEd, SAIF

Target Market(s)

parents of kids with dyslexia

Industry/Entity Type

Business

Contact Information for Business Card

Maple Path Learning of NH
Carla Whitmore - Dyslexia Diagnostician/Consultant
42 Tilbury Lane Londonderry, NH 03071
Phone (603)284-7105
WWW.MaplePathLearningofNH-example.com
MaplePathLearningofNH@mailbox-example.com

Requirements
Nice to have
• can have 2 sides not essential though

maybe "dyslexia" in the background spelled wrong or letters backward

```html
<!DOCTYPE html>
<html lang="en">
<head>
<meta charset="utf-8">
<title>Dyslexia Diagnostician – Business Card</title>
<link rel="stylesheet" href="https://fonts.googleapis.com/css2?family=Open+Sans:wght@400;600;700&display=swap">
<style>
  :root {
    --backdrop: #2b2b2b;
    --card-black: #050505;
    --card-blue: #1f8fcf;
    --card-light: #e4e4e4;
    --text-white: #ffffff;
  }
  html, body {
    margin: 0;
    width: 1200px;
    height: 900px;
    overflow: hidden;
    background: var(--backdrop);
    font-family: "Open Sans", Arial, sans-serif;
  }
  .business-card {
    position: absolute;
    left: 100px;
    top: 164px;
    width: 1000px;
    height: 572px;
    background: var(--card-light);
    overflow: hidden;
    box-shadow: 0 20px 40px rgba(0,0,0,0.45);
  }
  .card-shapes {
    position: absolute;
    inset: 0;
  }
  .card-content {
    position: absolute;
    left: 70px;
    top: 52px;
    color: var(--text-white);
  }
  .card-title {
    margin: 0;
    font-size: 46px;
    font-weight: 700;
    line-height: 1.1;
    letter-spacing: 0.2px;
    display: inline-block;
    padding-bottom: 6px;
    border-bottom: 2px solid var(--text-white);
  }
  .card-title .accent {
    color: var(--card-blue);
  }
  .card-name {
    margin: 6px 0 28px;
    font-size: 34px;
    font-weight: 700;
    line-height: 1.2;
  }
  .contact-list {
    list-style: none;
    margin: 0;
    padding: 0;
  }
  .contact-item {
    display: flex;
    align-items: center;
    gap: 16px;
    font-size: 27px;
    font-weight: 600;
    line-height: 46px;
  }
  .contact-icon {
    width: 22px;
    height: 22px;
    flex: none;
    fill: var(--text-white);
    stroke: var(--text-white);
  }
  .contact-item.no-icon {
    padding-left: 38px;
  }
</style>
</head>
<body>
  <div class="business-card">
    <svg class="card-shapes" viewBox="0 0 1000 572" preserveAspectRatio="none" aria-hidden="true">
      <path class="blue-swoosh" d="M0 0 H1000 V40 C990 360 720 600 0 556 Z" fill="var(--card-blue)"/>
      <path class="black-field" d="M0 0 H935 C950 300 700 560 0 525 Z" fill="var(--card-black)"/>
    </svg>

    <div class="card-content">
      <h1 class="card-title">Dyslexia <span class="accent">Diagnostician</span></h1>
      <p class="card-name">NH Carla Whitmore</p>
      <ul class="contact-list">
        <li class="contact-item">
          <svg class="contact-icon" viewBox="0 0 24 24" aria-hidden="true"><path d="M12 3 L2 12 H5 V21 H10 V15 H14 V21 H19 V12 H22 Z" stroke="none"/></svg>
          42 Tilbury Lane Londonderry, NH 03071
        </li>
        <li class="contact-item">
          <svg class="contact-icon" viewBox="0 0 24 24" aria-hidden="true"><g fill="none" stroke-width="2"><circle cx="12" cy="12" r="9"/><ellipse cx="12" cy="12" rx="4" ry="9"/><path d="M3 12 H21 M5 7 H19 M5 17 H19"/></g></svg>
          WWW.MaplePathLearningofNH-example.com
        </li>
        <li class="contact-item">
          <svg class="contact-icon" viewBox="0 0 24 24" aria-hidden="true"><rect x="2" y="5" width="20" height="14" rx="2" stroke="none"/><path d="M3 6 L12 13 L21 6" fill="none" stroke="var(--card-black)" stroke-width="2"/></svg>
          MaplePathLearningofNH@mailbox-example.com
        </li>
        <li class="contact-item">
          <svg class="contact-icon" viewBox="0 0 24 24" aria-hidden="true"><path d="M6.6 10.8 a15 15 0 0 0 6.6 6.6 l2.2-2.2 a1 1 0 0 1 1-.25 11.4 11.4 0 0 0 3.6.6 1 1 0 0 1 1 1 V20 a1 1 0 0 1-1 1 A17 17 0 0 1 3 4 a1 1 0 0 1 1-1 h3.5 a1 1 0 0 1 1 1 11.4 11.4 0 0 0 .6 3.6 1 1 0 0 1-.25 1 Z" stroke="none"/></svg>
          (603)284-7105
        </li>
      </ul>
    </div>
  </div>
</body>
</html>
```